Velmoro 25 years

Our company produces cognac – wine distillates, aged 3 years, 5 years, 7 years, 10 years, 15 years and 20 years.
More info you can find on http://www.velmoro-example.md/?lang=en

Project ”Velmoro 25 ani” is a new distilates that is 25 years old.

Product - 25 years Brandy
Scope of the project:
- Development of visual identity for a new brandy/cognac/distillates.

Background:
- The possibility of producing 25 years brandy, which will become an exclusive product in the assortment of Velmoro brandy

Market:
- The Republic of Moldova, Romania, China and Nigeria.

Price segment:
Premium

Target consumer:
Men aged 35-60, with a high income, who prefer hard drinks and are interested in buying a premium product for themselves or to give it as a gift in a show of respect.

Design tasks:

- Label and counter-label
- Souvenir box

Product Description:
Expensive, unique look, accent on the details, the combination of different materials and effects. The label must be admired, analyzed, in other words, to be an object of art. It must emphasize the quality and maturity of the brandy, justify the price. It must look extraordinary, enough to be chosen as a gift for an important person.
Label/ Eticheta we are waiting for options

Bottle type and color:
We are waiting for options
It is important that there are variations bottles of the same model for the volume 0.5 and 0.75 ml

Cap:

```html
<!DOCTYPE html>
<html lang="en">
<head>
<meta charset="utf-8">
<title>Velmoro 25 years – Label</title>
<link rel="stylesheet" href="https://fonts.googleapis.com/css2?family=Libre+Baskerville:wght@400&family=Montserrat:wght@500&family=Shrikhand&family=Roboto:wght@400&display=swap">
<style>
  :root {
    --ink: #1f1212;
    --cream: #f6f1e2;
    --paper: #ffffff;
    --text-brown: #3b2c25;
  }
  html, body {
    margin: 0;
    padding: 0;
    width: 1200px;
    height: 1200px;
    overflow: hidden;
    background: var(--paper);
  }
  .canvas {
    position: relative;
    width: 1200px;
    height: 1200px;
    background: var(--paper);
  }
  .label-shape {
    position: absolute;
    inset: 0;
    width: 1200px;
    height: 1200px;
  }
  .line-center {
    position: absolute;
    left: 0;
    width: 1200px;
    text-align: center;
    transform: translateY(-50%);
    margin: 0;
  }
  .brand-name {
    top: 333px;
    font-family: "Libre Baskerville", Georgia, serif;
    font-weight: 400;
    font-size: 50px;
    letter-spacing: 1px;
    color: var(--ink);
  }
  .tagline {
    top: 428px;
    font-family: "Montserrat", Arial, sans-serif;
    font-weight: 500;
    font-size: 23px;
    letter-spacing: 0.5px;
    color: var(--text-brown);
  }
  .product-title {
    top: 614px;
    font-family: "Shrikhand", Georgia, cursive;
    font-weight: 400;
    font-size: 34px;
    color: var(--cream);
    white-space: nowrap;
  }
  .product-title .age {
    font-size: 54px;
    vertical-align: -4px;
  }
  .description {
    position: absolute;
    top: 826px;
    left: 434px;
    width: 332px;
    margin: 0;
    text-align: center;
    font-family: "Roboto", Arial, sans-serif;
    font-size: 9.4px;
    line-height: 14px;
    color: var(--ink);
  }
  .volume {
    top: 980px;
    font-family: "Montserrat", Arial, sans-serif;
    font-weight: 500;
    font-size: 18px;
    color: var(--ink);
  }
</style>
</head>
<body>
<main class="canvas">
  <svg class="label-shape" viewBox="0 0 720 720" xmlns="http://www.w3.org/2000/svg" aria-hidden="true">
    <!-- outer border -->
    <path fill="var(--ink)" d="M235,128 H255 V110 H290 Q360,72 430,110 H465 V128 H485 V300 Q512,360 485,420 V590 H465 V608 H430 Q360,648 290,608 H255 V590 H235 V420 Q208,360 235,300 Z"/>
    <!-- cream field -->
    <path fill="var(--cream)" d="M241,134 H261 V116 H292 Q360,81 428,116 H459 V134 H479 V302 Q503,360 479,418 V584 H459 V602 H428 Q360,639 292,602 H261 V584 H241 V418 Q217,360 241,302 Z"/>
    <!-- inner rule, top panel -->
    <path fill="none" stroke="var(--ink)" stroke-width="1.2" d="M249,290 V142 H268 V124 H295 Q360,92 425,124 H452 V142 H471 V290"/>
    <path fill="none" stroke="var(--ink)" stroke-width="1.2" d="M249,152 H300 M420,152 H471"/>
    <!-- inner rule, bottom panel -->
    <path fill="none" stroke="var(--ink)" stroke-width="1.2" d="M249,430 V576 H268 V594 H295 Q360,626 425,594 H452 V576 H471 V430"/>
    <path fill="none" stroke="var(--ink)" stroke-width="1.2" d="M249,566 H285 V578 H435 V566 H471"/>
    <!-- central band -->
    <path fill="var(--ink)" d="M243,290 H477 Q503,360 477,430 H243 Q217,360 243,290 Z"/>
    <path fill="none" stroke="var(--cream)" stroke-width="1.5" d="M250,298 H470 Q492,360 470,422 H250 Q228,360 250,298 Z"/>
    <!-- divider rules -->
    <path fill="none" stroke="var(--ink)" stroke-width="1.2" d="M300,461 H420 M283,467 H437 M300,473 H420"/>
  </svg>

  <p class="line-center brand-name">VELMORO</p>
  <p class="line-center tagline">MADE WITH LOVE</p>
  <h1 class="line-center product-title">Velmoro <span class="age">25</span> years</h1>

  <p class="description">Expensive, unique look, accent on the details, the combination of different materials and effects. The label must be admired, analyzed, in other words, to be an object of art. It must emphasize the quality and maturity of the brandy, justify the price. It must look extraordinary, enough to be chosen as a gift for an important person.<br>Label/ Eticheta we are waiting for options</p>

  <p class="line-center volume">75 ml</p>
</main>
</body>
</html>
```